Cannabis Company needs a packaging design for a 4x6 pouch

We need a design for a new cannabis company. Included is the logo in red. The logo color can change. Whatever color looks best with the design is what we'll use. The design can't include any cartoon characters or anything that may appeal to children. We have multiple products that are similar that will be using the same design. The pouch will contain 10 pyramid shaped gummies. The look we're going for is modern, simple, but eye catching. I included a handful of photos of packaging we like if that helps.

```html
<!DOCTYPE html>
<html lang="en">
<head>
<meta charset="utf-8">
<title>Veltra Mango Gummy Pouch</title>
<link rel="stylesheet" href="https://fonts.googleapis.com/css2?family=Bebas+Neue&family=Barlow+Condensed:wght@500;600;700&display=swap">
<style>
  :root {
    --teal: #4fd0b4;
    --teal-light: #6fdcc8;
    --mango-yellow: #f9d744;
    --mango-orange: #f3a53a;
    --deep-orange: #ea8410;
    --panel: #edf4fb;
    --accent: #f8b042;
    --stat: #df8610;
    --brand-red: #e4141b;
    --white: #ffffff;
  }
  * { margin: 0; padding: 0; box-sizing: border-box; }
  html, body { width: 700px; height: 1200px; overflow: hidden; }
  body { font-family: "Barlow Condensed", sans-serif; }

  .pouch {
    position: relative;
    width: 700px;
    height: 1200px;
    overflow: hidden;
  }
  .pouch-art {
    position: absolute;
    inset: 0;
    background:
      radial-gradient(circle at 12% 12%, var(--mango-yellow) 0 20%, transparent 21%),
      radial-gradient(circle at 85% 8%, var(--mango-yellow) 0 18%, transparent 19%),
      radial-gradient(circle at 8% 85%, var(--mango-yellow) 0 22%, transparent 23%),
      radial-gradient(circle at 78% 90%, var(--mango-yellow) 0 26%, transparent 27%),
      linear-gradient(160deg, var(--teal-light) 0%, var(--teal) 35%, var(--deep-orange) 60%, var(--teal) 100%);
  }

  .info-panel {
    position: absolute;
    left: 78px; top: 416px;
    width: 544px; height: 304px;
    background: var(--panel);
  }

  .brand-tag {
    position: absolute;
    left: 247px; top: 314px;
    width: 213px; height: 114px;
    background: var(--panel);
  }
  .brand-frame {
    position: absolute;
    left: 6px; top: 4px;
    width: 200px; height: 106px;
    border: 1.5px solid var(--brand-red);
    border-radius: 3px;
    display: flex;
    flex-direction: column;
    align-items: center;
    justify-content: center;
    gap: 2px;
    padding-top: 14px;
  }
  .brand-name {
    display: flex;
    align-items: center;
    gap: 8px;
    font-weight: 700;
    font-size: 38px;
    line-height: 1;
    color: var(--brand-red);
    letter-spacing: 1px;
  }
  .brand-dot {
    width: 12px; height: 12px;
    border-radius: 50%;
    background: var(--brand-red);
  }
  .brand-sub {
    font-weight: 500;
    font-size: 10.5px;
    letter-spacing: 2.6px;
    color: var(--brand-red);
  }

  .flavor {
    position: absolute;
    left: 78px; top: 434px;
    width: 544px;
    text-align: center;
    font-family: "Bebas Neue", sans-serif;
    font-size: 118px;
    line-height: 1;
    letter-spacing: 14px;
    padding-left: 14px;
    color: var(--accent);
  }

  .product-band {
    position: absolute;
    left: 114px; top: 555px;
    width: 467px; height: 46px;
    background: var(--accent);
    color: var(--white);
    font-weight: 700;
    font-size: 30px;
    letter-spacing: 4.5px;
    line-height: 46px;
    text-align: center;
  }

  .stat-row {
    position: absolute;
    left: 118px; top: 639px;
    width: 470px; height: 48px;
    color: var(--stat);
  }
  .stat {
    position: absolute;
    bottom: -2px;
    font-family: "Bebas Neue", sans-serif;
    line-height: 1;
    white-space: nowrap;
  }
  .stat-value { font-size: 44px; letter-spacing: 3px; }
  .stat-unit {
    font-family: "Barlow Condensed", sans-serif;
    font-weight: 700;
    font-size: 14px;
    letter-spacing: 2px;
    margin-left: 2px;
  }
  .stat-count { left: 0; }
  .stat-dose { left: 128px; }
  .stat-thc { left: 242px; letter-spacing: 6px; }
  .stat-divider {
    position: absolute;
    top: 0;
    width: 3px; height: 48px;
    background: var(--stat);
  }
  .divider-1 { left: 106px; }
  .divider-2 { left: 218px; }
  .divider-3 { left: 339px; }
  .age-warning {
    position: absolute;
    left: 361px; bottom: -1px;
    font-weight: 700;
    font-size: 15.5px;
    line-height: 16px;
    letter-spacing: 1.6px;
  }
</style>
</head>
<body>
  <main class="pouch">
    <div class="pouch-art" role="img" aria-label="Illustrated pattern of ripe yellow mangoes over flowing teal and orange waves"></div>

    <section class="info-panel"></section>

    <div class="brand-tag">
      <div class="brand-frame">
        <div class="brand-name"><span class="brand-dot"></span>veltra</div>
        <div class="brand-sub">CANNABIS COMPANY</div>
      </div>
    </div>

    <h1 class="flavor">MANGO</h1>
    <p class="product-band">Cannabis – infused gummy</p>

    <div class="stat-row">
      <span class="stat stat-count"><span class="stat-value">10</span><span class="stat-unit">count</span></span>
      <span class="stat-divider divider-1"></span>
      <span class="stat stat-dose"><span class="stat-value">50</span><span class="stat-unit">MG</span></span>
      <span class="stat-divider divider-2"></span>
      <span class="stat stat-thc stat-value">THC</span>
      <span class="stat-divider divider-3"></span>
      <p class="age-warning">21 + Not safe<br>for children</p>
    </div>
  </main>
</body>
</html>
```